Pharmacy ad

need 2 pharmacy ads for the phone book. one for Birchfield Pharmacy and one for Corvane Rx Pharmacy. Dimensions for ad is 4.75in x 4.667 in. please see attached examples of ad uploaded as well logos of each pharmacy

```html
<!DOCTYPE html>
<html lang="en">
<head>
<meta charset="utf-8">
<title>Birchfield Pharmacy – Directory Ad</title>
<link href="https://fonts.googleapis.com/css2?family=Lato:wght@400;700;900&family=Tinos:wght@400;700&display=swap" rel="stylesheet">
<style>
  :root {
    --brand-blue: #0a7dbd;
    --heading-blue: #1576b8;
    --ink: #2b2a3d;
    --grey-text: #8d8d8d;
    --footer-grey: #626265;
    --pill-grey: #6d6d70;
    --sun-yellow: #f8d22b;
    --tick-yellow: #f4c431;
    --fold-grey: #8a8a8c;
    --rule: #c9c9c9;
    --white: #ffffff;
  }
  * { margin: 0; padding: 0; box-sizing: border-box; }
  html, body { width: 1200px; height: 1180px; overflow: hidden; background: var(--white); }
  body { font-family: "Lato", Arial, sans-serif; color: var(--ink); }
  .ad { position: relative; width: 1200px; height: 1180px; overflow: hidden; background: var(--white); }

  .hero-photo {
    position: absolute; left: 0; top: 0; width: 1200px; height: 428px;
    background:
      linear-gradient(90deg, rgba(255,255,255,0.75) 0%, rgba(255,255,255,0.55) 40%, rgba(255,255,255,0) 62%),
      linear-gradient(180deg, #e9eef3 0%, #dfe6ec 45%, #e8e3e6 100%);
  }
  .hero-photo::after {
    content: ""; position: absolute; right: 0; top: 0; width: 470px; height: 100%;
    background: linear-gradient(90deg, rgba(240,242,246,0) 0%, #f1f2f5 35%, #eceef2 100%);
  }

  .brand { position: absolute; left: 110px; top: 180px; width: 450px; display: flex; align-items: center; justify-content: center; gap: 14px; }
  .brand-square { display: block; width: 26px; height: 26px; background: var(--ink); flex-shrink: 0; }
  .brand-name { font-weight: 700; font-size: 40px; line-height: 48px; color: var(--ink); white-space: nowrap; }

  .ribbon-fold { position: absolute; top: 395px; }
  .ribbon-fold.left { left: 40px; }
  .ribbon-fold.right { left: 631px; }
  .ribbon { position: absolute; left: 67px; top: 395px; width: 564px; height: 510px; }

  .services { position: absolute; left: 108px; top: 440px; list-style: none; }
  .services li { display: flex; align-items: center; height: 49.6px; font-size: 30px; color: var(--white); }
  .services svg { width: 22px; height: 22px; margin-right: 14px; flex-shrink: 0; }
  .services b { font-weight: 900; margin-right: 8px; }

  .payment-row { position: absolute; left: 97px; top: 944px; width: 510px; display: flex; align-items: center; justify-content: space-between; }
  .payment-name { display: flex; align-items: center; gap: 7px; font-weight: 700; font-size: 18px; color: var(--ink); white-space: nowrap; }
  .payment-name i { display: block; width: 14px; height: 14px; border-radius: 50%; background: var(--fold-grey); }

  .headline { position: absolute; left: 700px; top: 490px; width: 430px; font-family: "Tinos", "Times New Roman", serif; }
  .headline .lead { font-size: 58px; color: var(--grey-text); line-height: 62px; }
  .headline .accent { font-size: 62px; font-weight: 700; color: var(--heading-blue); text-align: right; line-height: 64px; }

  .offer { position: absolute; left: 683px; width: 472px; height: 73px; border-radius: 37px; text-align: center; padding-top: 6px; }
  .offer.senior { top: 663px; background: var(--sun-yellow); color: var(--ink); }
  .offer.student { top: 750px; background: var(--pill-grey); color: var(--white); }
  .offer strong { display: block; font-size: 30px; font-weight: 700; line-height: 34px; }
  .offer span { display: block; font-size: 21px; line-height: 26px; }

  .hours { position: absolute; left: 691px; top: 862px; width: 434px; }
  .hours div { height: 43.5px; font-size: 27px; line-height: 40px; color: var(--ink); white-space: nowrap; }
  .hours div + div { border-top: 2px solid var(--rule); }
  .hours b { font-weight: 700; }
  .hours small { font-size: 19px; }

  .footer { position: absolute; left: 0; top: 1018px; width: 1200px; height: 162px; background: var(--footer-grey); color: var(--white); }
  .branch { position: absolute; top: 26px; }
  .branch.main { left: 74px; }
  .branch.port { left: 508px; }
  .branch p { font-size: 30px; line-height: 36px; }
  .branch .note { font-size: 22px; line-height: 30px; }
  .branch .phone { font-size: 33px; font-weight: 900; line-height: 44px; }
  .social { position: absolute; left: 885px; top: 40px; display: flex; align-items: center; gap: 14px; }
  .social i { display: block; width: 70px; height: 70px; background: var(--brand-blue); border-radius: 8px; }
  .social .visit { font-size: 23px; line-height: 28px; }
  .social .name { font-size: 38px; font-weight: 900; line-height: 42px; }
</style>
</head>
<body>
<main class="ad">
  <div class="hero-photo" role="img" aria-label="Photo of a pharmacist in a white coat on the phone in front of shelves of medicines"></div>

  <div class="brand">
    <span class="brand-square"></span>
    <span class="brand-name">Birchfield Pharmacy</span>
  </div>

  <svg class="ribbon-fold left" width="27" height="34" viewBox="0 0 27 34"><polygon points="27,0 0,34 27,34" fill="var(--fold-grey)"/></svg>
  <svg class="ribbon-fold right" width="27" height="34" viewBox="0 0 27 34"><polygon points="0,0 27,34 0,34" fill="var(--fold-grey)"/></svg>
  <svg class="ribbon" viewBox="0 0 564 510"><polygon points="0,0 564,0 564,510 276,454 0,510" fill="var(--brand-blue)"/></svg>

  <ul class="services">
    <li><svg viewBox="0 0 22 22"><rect x="1.5" y="4.5" width="16" height="16" fill="none" stroke="var(--tick-yellow)" stroke-width="2"/><path d="M5 12l4 4 11-13" fill="none" stroke="var(--tick-yellow)" stroke-width="2.4"/></svg><b>Certified</b>Pharmacists</li>
    <li><svg viewBox="0 0 22 22"><rect x="1.5" y="4.5" width="16" height="16" fill="none" stroke="var(--tick-yellow)" stroke-width="2"/><path d="M5 12l4 4 11-13" fill="none" stroke="var(--tick-yellow)" stroke-width="2.4"/></svg><b>Affordable</b>prices</li>
    <li><svg viewBox="0 0 22 22"><rect x="1.5" y="4.5" width="16" height="16" fill="none" stroke="var(--tick-yellow)" stroke-width="2"/><path d="M5 12l4 4 11-13" fill="none" stroke="var(--tick-yellow)" stroke-width="2.4"/></svg>Brand and Generic Medicines</li>
    <li><svg viewBox="0 0 22 22"><rect x="1.5" y="4.5" width="16" height="16" fill="none" stroke="var(--tick-yellow)" stroke-width="2"/><path d="M5 12l4 4 11-13" fill="none" stroke="var(--tick-yellow)" stroke-width="2.4"/></svg>Blood Pressure and Glucose checks</li>
    <li><svg viewBox="0 0 22 22"><rect x="1.5" y="4.5" width="16" height="16" fill="none" stroke="var(--tick-yellow)" stroke-width="2"/><path d="M5 12l4 4 11-13" fill="none" stroke="var(--tick-yellow)" stroke-width="2.4"/></svg>Personal care and Beauty Products</li>
    <li><svg viewBox="0 0 22 22"><rect x="1.5" y="4.5" width="16" height="16" fill="none" stroke="var(--tick-yellow)" stroke-width="2"/><path d="M5 12l4 4 11-13" fill="none" stroke="var(--tick-yellow)" stroke-width="2.4"/></svg>Injectables</li>
    <li><svg viewBox="0 0 22 22"><rect x="1.5" y="4.5" width="16" height="16" fill="none" stroke="var(--tick-yellow)" stroke-width="2"/><path d="M5 12l4 4 11-13" fill="none" stroke="var(--tick-yellow)" stroke-width="2.4"/></svg>Special Orders</li>
    <li><svg viewBox="0 0 22 22"><rect x="1.5" y="4.5" width="16" height="16" fill="none" stroke="var(--tick-yellow)" stroke-width="2"/><path d="M5 12l4 4 11-13" fill="none" stroke="var(--tick-yellow)" stroke-width="2.4"/></svg>Delivery service</li>
  </ul>

  <div class="payment-row">
    <span class="payment-name"><i></i>Cardwise</span>
    <span class="payment-name"><i></i>Paylo</span>
    <span class="payment-name"><i></i>Harbourline Life</span>
    <span class="payment-name"><i></i>Keelmark</span>
  </div>

  <div class="headline">
    <div class="lead">We care about</div>
    <div class="accent">your Health</div>
  </div>

  <div class="offer senior"><strong>10 % senior citizen discount</strong><span>For patients 60 years and over</span></div>
  <div class="offer student"><strong>10 % Student discount</strong><span>With valid ID card</span></div>

  <div class="hours">
    <div><b>Monday Friday</b> 10am- 6pm</div>
    <div><b>Saturday</b> 10am-5pm</div>
    <div><b>Sunday</b> 10am-2pm <small>(Ferrow Street branch)</small></div>
  </div>

  <footer class="footer">
    <div class="branch main">
      <p>27 Ferrow Street, Lindenport</p>
      <p class="note">(opposite Grace Harbour Church)</p>
      <p class="phone">Phone: 555-0174</p>
    </div>
    <div class="branch port">
      <p>Quay Point, Food Court,</p>
      <p>Lindenport</p>
      <p class="phone">Phone: 555-0177</p>
    </div>
    <div class="social">
      <i></i>
      <div>
        <div class="visit">visit us on</div>
        <div class="name">Chatterly</div>
      </div>
    </div>
  </footer>
</main>
</body>
</html>
```